Card Design

We are looking for a mailing for a small business that is helping other small businesses conform to new provincial legislation regarding accessibility in the workplace.
The size will be 4" x 6"
This will be mass mailed through the post office so there is no need to included space for recipient address.
Front/Style: Professional/Official
Text:
As of right now, all businesses in Ontario that employ ONE OR MORE people, must comply with the Accessibilty for Ontarians with Disability Act. INCLUDING MANATORY STAFF TRAINING. (You can include an image if works with the overall look).
- We are trying to convey the idea that they need to act now.
Back
Font / Style: Professional but less official than the front.
Text:
Compliance Checklist
(please put a small box in front of each * sign)
Does your company employ ONE or more business
* Yes * No
If yes, then as of January 1,2012, your business must:
* Establish accessibility policies, practicesn and procedures
* Allow guide dogs, service animals and/or support persons onto the premises.
*Provide notice of temporary disruptions facilities and services.
*Provide training to staff.
* Establish a process for receiving and responding to accessibility feedback.
* Documentation must be kept on file
*Annual Accessibility report to the Ministry.
GET COMPLIANT NOW
Tallowmere Consulting has produced a *Steadfast Rulebook Bundle Set to help business to become compliant with the Accessibility Standard for Customer Service.
Contact us at
1-855-3179504 (AODA)
email : info@tallowmereconsulting.ca
or tallowmereconsulting.ca

```html
<!DOCTYPE html>
<html lang="en">
<head>
<meta charset="utf-8">
<title>Accessibility Compliance Mailer</title>
<link href="https://fonts.googleapis.com/css2?family=Arimo:wght@400;700&family=Source+Sans+3:wght@400;600;700&display=swap" rel="stylesheet">
<style>
  :root {
    --stage: #3a2c25;
    --card: #ffffff;
    --band-grey: #d6d6d6;
    --ink: #2b2b2b;
    --ink-soft: #3c3c3c;
    --accent-red: #c0272d;
    --box-border: #8a2a2a;
    --panel-dark: #3d3735;
    --panel-light: #f1f1f1;
    --rule: #dcdcdc;
  }
  * { box-sizing: border-box; margin: 0; padding: 0; }
  html, body { width: 1200px; height: 513px; overflow: hidden; }
  body { background: var(--stage); position: relative; }

  .card {
    position: absolute;
    background: var(--card);
    box-shadow: 0 2px 6px rgba(0,0,0,.35);
  }

  /* Front */
  .card-front { left: 92px; top: 53px; width: 533px; height: 353px; }
  .photo-strip {
    position: absolute; left: 0; right: 0; top: 27px; height: 190px;
    display: flex; gap: 3px; padding: 0 2px;
    background: var(--card);
  }
  .photo { flex: 1; height: 100%; }
  .photo-team { background: linear-gradient(135deg, #6b5a52 0%, #c9a58e 45%, #e6e1dc 100%); }
  .photo-hands { background: linear-gradient(160deg, #e9ecef 0%, #c7b3a2 50%, #8e9aa6 100%); }
  .photo-office { background: linear-gradient(120deg, #b9c6d3 0%, #eceff2 45%, #3f4650 100%); }
  .grey-band { position: absolute; left: 0; right: 0; top: 217px; height: 9px; background: var(--band-grey); }
  .front-message {
    position: absolute; left: 0; right: 0; top: 236px;
    text-align: center;
    font-family: "Arimo", Arial, sans-serif;
    font-size: 13px; line-height: 19px; color: var(--ink);
    text-transform: uppercase;
  }
  .front-message strong { font-weight: 700; }

  /* Back */
  .card-back { left: 578px; top: 104px; width: 530px; height: 352px; font-family: "Source Sans 3", Arial, sans-serif; }
  .checklist { position: absolute; left: 0; right: 0; top: 0; height: 201px; padding: 12px 18px 0; color: var(--ink-soft); }
  .question { color: var(--accent-red); font-weight: 700; font-size: 11px; }
  .answers { display: flex; gap: 22px; margin: 9px 0 0 8px; font-size: 12px; align-items: center; }
  .answer { display: flex; align-items: center; gap: 6px; }
  .tickbox { width: 14px; height: 14px; border: 1.5px solid var(--box-border); border-radius: 3px; background: #f7f2f2; }
  .divider { height: 1px; background: var(--rule); margin: 6px -18px 0 0; }
  .lead { font-size: 11px; font-weight: 600; margin-top: 6px; }
  .lead em { font-style: normal; color: var(--accent-red); font-weight: 700; }
  .duties { list-style: none; font-size: 11px; line-height: 16.6px; margin-top: 1px; }

  .promo { position: absolute; left: 0; right: 0; top: 203px; bottom: 0; display: flex; }
  .brand {
    width: 146px; background: linear-gradient(180deg, #ffffff, var(--panel-light));
    display: flex; flex-direction: column; align-items: center; justify-content: center; gap: 8px;
  }
  .brand-mark { width: 22px; height: 22px; background: var(--accent-red); }
  .brand-name { font-weight: 600; font-size: 13px; color: var(--accent-red); text-align: center; line-height: 15px; text-transform: uppercase; }
  .offer { flex: 1; background: var(--panel-dark); color: #fff; text-align: center; padding-top: 6px; font-size: 11px; line-height: 13.5px; }
  .offer h2 { font-size: 18px; font-weight: 700; line-height: 22px; margin-bottom: 2px; }
  .offer .contact-title { font-size: 13px; margin-top: 5px; line-height: 17px; }
</style>
</head>
<body>

<section class="card card-front">
  <div class="photo-strip">
    <div class="photo photo-team" role="img" aria-label="Smiling businesswoman with colleagues in an office"></div>
    <div class="photo photo-hands" role="img" aria-label="Team members joining raised hands together"></div>
    <div class="photo photo-office" role="img" aria-label="Confident businesswoman standing in front of her team"></div>
  </div>
  <div class="grey-band"></div>
  <p class="front-message">
    As of right now,<br>
    all businesses in Ontario that employ<br>
    one or more people, must comply<br>
    with the Accessibilty for Ontarians with<br>
    Disability Act.<br>
    <strong>Including manatory staff training</strong>
  </p>
</section>

<section class="card card-back">
  <div class="checklist">
    <p class="question">Does your company employ ONE or more business</p>
    <div class="answers">
      <span class="answer"><span class="tickbox"></span>Yes</span>
      <span class="answer"><span class="tickbox"></span>No</span>
    </div>
    <div class="divider"></div>
    <p class="lead">If yes, then as of January 1,2012, your business <em>must:</em></p>
    <ul class="duties">
      <li>* Establish accessibility policies, practicesn and procedures</li>
      <li>* Allow guide dogs, service animals and/or support persons onto the premises.</li>
      <li>*Provide notice of temporary disruptions facilities and services.</li>
      <li>*Provide training to staff.</li>
      <li>* Establish a process for receiving and responding to accessibility feedback.</li>
      <li>* Documentation must be kept on file</li>
      <li>*Annual Accessibility report to the Ministry.</li>
    </ul>
  </div>
  <div class="promo">
    <div class="brand">
      <span class="brand-mark"></span>
      <span class="brand-name">Tallowmere<br>Consulting Inc.</span>
    </div>
    <div class="offer">
      <h2>GET COMPLIANT NOW</h2>
      <p>Tallowmere Consulting has poduced a *Steadfast Rulebook Bundle Set<br>to help business to become compliant with the<br>Accessibility Standard for Customer Service.</p>
      <p class="contact-title">Contact us at</p>
      <p>1-855-3179504 (AODA)<br>email : info@tallowmereconsulting.ca<br>or www.tallowmereconsulting.ca</p>
    </div>
  </div>
</section>

</body>
</html>
```